Off Grid consulting and outdoor products needs a website

We need a website design to help launch our new business. Its a business that plans to offer Off-grid conslting and outdoor survival products to people who are looking to relocate or vacation to properties/homes that are Off-grid. We plan to offer design plans for homes/cabins, renewable energy systems for power/heating etc, survival products for outdoor vacations/living. We also do consulting and project management for those who want to design and build from scratch their dream off-grid home or vacation property. I've included our logo design for use.
Would like the website to include 5 pages.
www.ridgepinehaven.com
The main landing page (1)
want a video loop backround with a flyover of a cabin in the woods.
https://www.clipvaultora.com/video/clip-48291736-blue-sky-melting-snow-on-green-energy
(also need a backup static image of just high-shot of cabin in woods)
logo top left, Quoted string of text in the middle, over the video. and a CTA button to 'Contact us'
picture links below that to last 3 recent blog posts.
About Us page (2)
(example) https://larkwildgear.com/pages/about-lark
Blog page (3)
blog posts associated with pictures.
Consulting 'services' page (4)
-land services and moving off-grid
-Building off grid
-Renewable energy off-grid
-Sustainable farming and all season greenhouses
Store page 'comming soon' (5)
(Example) http://timberly.crestlayouts.com/demo-1/demo.html

Target Market(s)

Outdoor enthusiasts and people who want to escape their city life

Coding

Coded - Design and coding required

Requirements
Must have
• Outdoor feel, woods, cabin, reneable energy (solar, geothermal, greenhouses, water wells)

```html
<!DOCTYPE html>
<html lang="en">
<head>
<meta charset="utf-8">
<title>Ridge Pine Haven — Off Grid Consulting</title>
<link href="https://fonts.googleapis.com/css2?family=Barlow+Condensed:ital,wght@1,800&family=Poppins:wght@400;500;600;700&display=swap" rel="stylesheet">
<style>
:root{
  --amber:#cc8400;
  --rust:#a4522a;
  --charcoal:#333333;
  --ink:#2b2b2b;
  --white:#ffffff;
  --rule:#8a8a8a;
  --muted:#555555;
}
*{box-sizing:border-box;margin:0;padding:0}
html,body{width:1200px;height:3350px;overflow:hidden}
body{position:relative;font-family:"Poppins",sans-serif;background:var(--white);color:var(--ink)}
.abs{position:absolute}
.display{font-family:"Barlow Condensed",sans-serif;font-style:italic;font-weight:800;font-size:50px;line-height:1;letter-spacing:.5px}
.btn{position:absolute;display:flex;align-items:center;justify-content:center;background:var(--amber);color:var(--white);border-radius:24px;font-size:14px}

/* hero */
.hero{left:0;top:0;width:1200px;height:540px;background:linear-gradient(180deg,#6f7f95 0%,#4f5a63 22%,#2f3a33 45%,#1f2a24 75%,#26302b 100%)}
.hero-curve{left:0;top:320px;width:1200px;height:240px}
.brand{font-weight:600;font-size:19px;line-height:1.1}
.nav a{position:absolute;top:45px;font-size:14px;color:var(--white);text-decoration:none}
.play{left:569px;top:175px;width:62px;height:62px;border-radius:50%;background:var(--white);box-shadow:0 0 0 4px rgba(255,255,255,.35)}
.hero-title{left:0;width:1200px;top:258px;text-align:center;color:var(--white);font-weight:700;font-size:25.5px}
.hero-sub{left:0;width:1200px;top:293px;text-align:center;color:var(--white);font-size:22px;line-height:30px;text-transform:uppercase}

/* about */
.about-box{left:160px;top:655px;width:528px;height:493px;background:var(--charcoal)}
.about-title{left:216px;top:757px;color:var(--amber)}
.about-text{left:216px;top:822px;width:426px;color:var(--white);font-size:14.2px;line-height:25.7px}
.about-photo{left:688px;top:745px;width:351px;height:360px;background:linear-gradient(160deg,#3b4a3a,#1f2a22 55%,#6a4526 80%,#2a2a22)}

/* services */
.services{left:0;top:1252px;width:1200px;height:598px;background:linear-gradient(180deg,#3d3d3e 0%,#5a5f68 30%,#4d5561 60%,#39414c 100%)}
.services-title{left:0;width:1200px;top:1344px;text-align:center;color:var(--white)}
.svc-photo{top:1421px;width:213px;height:264px}
.svc-label{top:1702px;width:213px;text-align:center;color:var(--white);font-size:17px;line-height:25px}

/* blog */
.blog-title{left:0;width:1162px;top:1948px;text-align:center;color:var(--amber)}
.blog-card{left:160px;top:2028px;width:879px;height:358px;background:var(--amber)}
.blog-photo{left:184px;top:2049px;width:274px;height:317px;background:linear-gradient(180deg,#c0701f,#8a4a1c 45%,#3e2417 80%,#2a1a12)}
.blog-head{left:502px;top:2079px;width:300px;color:var(--white);font-weight:700;font-size:17px;line-height:25px}
.blog-text{left:502px;top:2134px;width:500px;color:var(--white);font-size:14px;line-height:25.7px}
.blog-date{left:502px;top:2308px;color:var(--white);font-size:14px;display:flex;align-items:center;gap:8px}
.arrow{width:46px;height:46px;border-radius:50%;display:flex;align-items:center;justify-content:center}

/* inquiry */
.inquiry{left:0;top:2497px;width:688px;height:501px;background:linear-gradient(180deg,#fafafa,#f1f1f1 50%,#fafafa);box-shadow:0 0 30px rgba(0,0,0,.06)}
.inquiry-title{left:162px;top:2594px;color:var(--charcoal)}
.field{height:28px;border-bottom:1px solid var(--muted);font-size:14.5px;display:flex;align-items:center;gap:6px}
.inquiry-photo{left:688px;top:2548px;width:512px;height:400px;background:linear-gradient(180deg,#4a4f44,#3a3f33 40%,#5a3524 70%,#2f3426)}

/* footer */
.foot-nav a{position:absolute;top:3098px;font-size:14px;color:var(--ink);text-decoration:none}
.foot-rule{left:160px;top:3187px;width:879px;height:1px;background:var(--rule)}
.foot-item{font-size:14.5px;line-height:22px;display:flex;align-items:center;gap:8px}
.divider{top:3204px;width:1px;height:44px;background:var(--rule)}
.bottom-bar{left:0;top:3300px;width:1200px;height:50px;background:var(--charcoal);color:var(--white);font-size:14.5px}
</style>
</head>
<body>

<!-- hero -->
<section class="abs hero" role="img" aria-label="Aerial video loop of a snowy cabin in a pine forest with mountains"></section>
<div class="abs brand" style="left:160px;top:38px;color:var(--white)">Ridge Pine<br>Haven</div>
<nav class="nav">
  <a style="left:468px">Home</a>
  <a style="left:583px">About Us</a>
  <a style="left:720px">Services</a>
  <a style="left:851px">Blogs</a>
  <a style="left:963px">Contact Us</a>
</nav>
<div class="abs play">
  <svg width="62" height="62" viewBox="0 0 62 62"><path d="M25 19 L43 31 L25 43 Z" fill="var(--rust)"/></svg>
</div>
<h1 class="abs hero-title">WE OFFER OFF GRID CONSULTING &amp; OUTDOOR SURVIVAL PRODUCTS</h1>
<p class="abs hero-sub">To people who are looking to relocate or vacation to homes<br>that are off grid / away from city</p>
<a class="btn" style="left:525px;top:370px;width:150px;height:44px">Contact Us</a>
<svg class="abs hero-curve" viewBox="0 0 1200 240" preserveAspectRatio="none">
  <path d="M0 20 C250 180 450 210 620 210 C850 210 1050 140 1200 80 L1200 240 L0 240 Z" fill="var(--rust)"/>
  <path d="M0 20 C250 160 450 200 620 200 C850 200 1050 130 1200 70 L1200 88 C1050 150 850 214 620 214 C450 214 250 185 0 40 Z" fill="var(--amber)"/>
  <path d="M0 44 C250 190 450 220 620 220 C850 220 1050 152 1200 92 L1200 240 L0 240 Z" fill="var(--white)"/>
</svg>

<!-- about -->
<section class="abs about-box"></section>
<h2 class="abs display about-title">About Us</h2>
<p class="abs about-text">Lorem ipsum dolor sit amet, consectetuer adipiscing elit, sed diam nonummy nibh euismod tincidunt ut laoreet dolore magna aliquam erat volutpat. Ut wisi enim ad minim veniam, quis nostrud exerci tation ullamcorper suscipit lobortis nisl ut aliquip ex ea commodo consequat. Duis autem vel eum iriure dolor in hendrerit in vulputate velit esse molestie</p>
<a class="btn" style="left:216px;top:1000px;width:134px;height:44px">Read More</a>
<div class="abs about-photo" role="img" aria-label="Lit A-frame cabin among tall forest trees at dusk"></div>

<!-- services -->
<section class="abs services" role="img" aria-label="Snowy forest with autumn trees seen from above"></section>
<h2 class="abs display services-title">Our Services</h2>
<div class="abs svc-photo" style="left:160px;background:linear-gradient(180deg,#7d8a90,#6a4a2c 60%,#3a2a1e)" role="img" aria-label="Modern timber cabin with large windows"></div>
<div class="abs svc-photo" style="left:382px;background:linear-gradient(180deg,#5b5f5c,#6d4c34 55%,#4c5a32)" role="img" aria-label="Wooden barn with solar panels on the roof"></div>
<div class="abs svc-photo" style="left:604px;background:linear-gradient(180deg,#4f8aa6,#8a8f86 55%,#6b5a3e)" role="img" aria-label="Small off grid home under a large tree"></div>
<div class="abs svc-photo" style="left:826px;background:linear-gradient(180deg,#7a8a6a,#6a3e24 50%,#2f4a2a)" role="img" aria-label="Wooden cabin surrounded by lush garden plants"></div>
<p class="abs svc-label" style="left:160px">Land Services And<br>Moving Off-grid</p>
<p class="abs svc-label" style="left:382px">Renewable Energy<br>Off-grid</p>
<p class="abs svc-label" style="left:604px">Building Off Grid</p>
<p class="abs svc-label" style="left:826px">Sustainable Farming &amp;<br>All Season Greenhouses</p>

<!-- blog -->
<h2 class="abs display blog-title">Blog Posts</h2>
<svg class="abs" style="left:150px;top:2005px" width="900" height="410" viewBox="0 0 900 410">
  <path d="M10 28 L880 0 L898 368 L20 406 Z" fill="var(--rust)"/>
</svg>
<section class="abs blog-card"></section>
<div class="abs blog-photo" role="img" aria-label="Rustic log cabin in an autumn forest"></div>
<h3 class="abs blog-head">Lorem ipsum dolor amet, consectetuer</h3>
<p class="abs blog-text">Lorem ipsum dolor sit &nbsp; adipiscing elit, sed diam nonummy nibh euismod tincidunt ut laoreet dolore magna aliquam. Lorem ipsum dolor sit adipiscing elit, sed diam nonummy nibh euismod tincidunt ut laoreet dolore magna aliquam .Lorem ipsum dolor sit &nbsp; adipiscing elit, sed diam nonummy nibh euismod tincidunt.</p>
<p class="abs blog-date">
  <svg width="20" height="20" viewBox="0 0 20 20" fill="none" stroke="#fff" stroke-width="1.5"><rect x="2" y="4" width="14" height="13" rx="1.5"/><path d="M2 8h14M6 2v4M12 2v4"/><circle cx="15" cy="15" r="4" fill="var(--amber)"/><path d="M15 13v2l1.3 1"/></svg>
  14th Apr 2022, 8:30 am
</p>
<div class="abs arrow" style="left:86px;top:2184px;border:1.5px solid var(--ink)">
  <svg width="10" height="10" viewBox="0 0 10 10"><path d="M6.5 1.5 L3 5 L6.5 8.5" fill="none" stroke="var(--ink)" stroke-width="1.5"/></svg>
</div>
<div class="abs arrow" style="left:1068px;top:2184px;background:var(--rust)">
  <svg width="10" height="10" viewBox="0 0 10 10"><path d="M3.5 1.5 L7 5 L3.5 8.5" fill="none" stroke="#fff" stroke-width="1.5"/></svg>
</div>

<!-- inquiry -->
<section class="abs inquiry"></section>
<h2 class="abs display inquiry-title">Quick Inquiry</h2>
<div class="abs field" style="left:162px;top:2666px;width:476px">
  <svg width="12" height="12" viewBox="0 0 12 12"><circle cx="6" cy="3.5" r="3" fill="var(--ink)"/><path d="M0 12c0-4 3-5.5 6-5.5s6 1.5 6 5.5z" fill="var(--ink)"/></svg>Name</div>
<div class="abs field" style="left:162px;top:2726px;width:222px">
  <svg width="13" height="10" viewBox="0 0 13 10"><rect width="13" height="10" fill="var(--ink)"/><path d="M0 0l6.5 5L13 0" stroke="#fff" fill="none"/></svg>Email</div>
<div class="abs field" style="left:414px;top:2726px;width:224px">
  <svg width="12" height="12" viewBox="0 0 12 12"><path d="M2 0l2.5 3-1.5 1.5c.8 1.8 2.2 3.2 4 4L8.5 7l3 2.5L10 12C4.5 11.5.5 7.5 0 2z" fill="var(--ink)"/></svg>Phone</div>
<div class="abs field" style="left:162px;top:2786px;width:476px">
  <svg width="12" height="11" viewBox="0 0 12 11"><path d="M0 1h12M0 4h12M0 7h12M0 10h8" stroke="var(--ink)" stroke-width="1.5"/></svg>Message</div>
<a class="btn" style="left:162px;top:2853px;width:120px;height:45px">Submit</a>
<div class="abs inquiry-photo" role="img" aria-label="Log cabin with stone chimney in a mossy forest"></div>

<!-- footer -->
<div class="abs brand" style="left:160px;top:3094px;color:var(--ink)">Ridge Pine<br>Haven</div>
<nav class="foot-nav">
  <a style="left:466px">Home</a>
  <a style="left:580px">About Us</a>
  <a style="left:717px">Services</a>
  <a style="left:848px">Blogs</a>
  <a style="left:960px">Contact Us</a>
</nav>
<div class="abs foot-rule"></div>
<div class="abs foot-item" style="left:160px;top:3203px">
  <svg width="24" height="26" viewBox="0 0 24 26" fill="none" stroke="var(--ink)" stroke-width="1.2"><circle cx="10" cy="15" r="9"/><path d="M1 15h18M10 6c-3 3-3 15 0 18M10 6c3 3 3 15 0 18"/><path d="M18 1a4 4 0 0 1 4 4c0 3-4 7-4 7s-4-4-4-7a4 4 0 0 1 4-4z" fill="#fff"/><circle cx="18" cy="5" r="1.3"/></svg>
  <span>123, Street Name,<br>Country Name, Pincode</span>
</div>
<div class="abs divider" style="left:443px"></div>
<div class="abs foot-item" style="left:530px;top:3214px">
  <svg width="22" height="22" viewBox="0 0 22 22" fill="none" stroke="var(--ink)" stroke-width="1.2"><path d="M4 3l4 4-2 2.5c1.5 3 3.5 5 6.5 6.5L15 14l4 4-2.5 2.5C9 19.5 2.5 13 1.5 5.5z"/><path d="M13 2a7 7 0 0 1 7 7M13 5a4 4 0 0 1 4 4"/></svg>
  123-456-7890
</div>
<div class="abs divider" style="left:752px"></div>
<div class="abs foot-item" style="left:840px;top:3214px">
  <svg width="20" height="14" viewBox="0 0 20 14" fill="none" stroke="var(--ink)" stroke-width="1.2"><rect x=".6" y=".6" width="18.8" height="12.8"/><path d="M.6.6L10 8 19.4.6M.6 13.4l7-6.5M19.4 13.4l-7-6.5"/></svg>
  info@ridgepinehaven.com
</div>
<footer class="abs bottom-bar">
  <span class="abs" style="left:162px;top:14px">Copyright © 2022 Ridge Pine Haven. All Rights Reserved.</span>
  <span class="abs" style="left:990px;top:18px;width:12px;height:12px;border-radius:50%;background:var(--white)"></span>
  <span class="abs" style="left:1024px;top:18px;width:12px;height:12px;border-radius:50%;background:var(--white)"></span>
</footer>

</body>
</html>
```